Brightnest Dwelling Stationery Design

Letterpaper, business cards, notebook, envelope A4 & A5

Target Market(s)

Business, accommodation, hotels, flexible housing

Font styles to use
Other font styles liked:
• Montserrat

Colors

Designer to choose only greyscale colors for use in the design.

Requirements
Must have
• Luxurious appearance
Keep it simple, just like the logo
Modern
Nice to have
• Tight Luxury Design
Should not have
• Illustrations
Decorative

```html
<!DOCTYPE html>
<html lang="en">
<head>
<meta charset="utf-8">
<title>Brightnest Dwelling Stationery</title>
<link href="https://fonts.googleapis.com/css2?family=Montserrat:wght@300;400;500;600&display=swap" rel="stylesheet">
<style>
:root{
  --ink:#111111;
  --black:#0d0d0d;
  --charcoal:#1c1c1c;
  --paper:#ffffff;
  --paper-soft:#f6f6f6;
  --grey-line:#9a9a9a;
  --grey-text:#555555;
  --bg-light:#ececec;
  --bg-mid:#d6d6d6;
  --bg-note:#e3e3e3;
  --faint:#dcdcdc;
}
*{box-sizing:border-box;margin:0;padding:0}
html,body{width:1200px;height:3319px;overflow:hidden}
body{position:relative;font-family:'Montserrat',sans-serif;color:var(--ink);background:var(--bg-light)}
.section{position:absolute;left:0;width:1200px}
.section--cards{top:0;height:795px;background:var(--charcoal)}
.section--suite{top:795px;height:752px;background:var(--bg-light)}
.section--a4{top:1547px;height:883px;background:var(--bg-mid)}
.section--notebook{top:2430px;height:889px;background:var(--bg-note)}
.item{position:absolute}
.shadow{box-shadow:0 6px 18px rgba(0,0,0,.18)}

/* brand name block */
.brand{display:flex;flex-direction:column;align-items:center;gap:.45em}
.brand__square{width:2.4em;height:2.4em;border:1.5px solid currentColor}
.brand__name{font-weight:400;letter-spacing:.12em;text-align:center;line-height:1.35;text-transform:uppercase}

/* business card */
.card{background:var(--paper);padding:26px 30px;display:flex;flex-direction:column;justify-content:space-between}
.card__top{display:flex;justify-content:flex-end}
.card__rule{height:1px;background:var(--grey-line);margin:6px 0}
.card__bottom{display:flex;justify-content:space-between;align-items:flex-end}
.card__person-name{font-weight:600;font-size:17px;letter-spacing:.04em;text-transform:uppercase}
.card__person-role{font-size:11px;color:var(--grey-text);margin:2px 0 10px}
.contact{list-style:none;font-size:11px;line-height:1.6}
.contact li{display:flex;align-items:center;gap:7px}
.contact svg{width:10px;height:10px;flex:none}
.card__address{font-size:11px;text-align:right;line-height:1.5;color:var(--grey-text)}
.card-back{background:var(--black)}

/* letterhead */
.letter{background:var(--paper);display:flex;flex-direction:column}
.letter__body{font-size:5.2px;line-height:1.55;color:#444}
.letter__body p{margin-bottom:6px}
.letter__foot{margin-top:auto;display:flex;justify-content:space-between;font-size:5.2px;line-height:1.5;color:#444}
.signature{width:22px;height:14px;background:#e4e4e8;margin:4px 0 8px}

/* folder */
.folder{background:var(--black);color:var(--paper);display:flex;flex-direction:column;align-items:center}
.folder__band{margin-top:auto;width:100%;height:26px;background:var(--paper);display:flex;align-items:center;justify-content:center;font-size:8.5px;font-weight:600;letter-spacing:.12em;border-top:6px solid var(--black);border-bottom:8px solid var(--black)}

.envelope{background:var(--paper-soft)}
.envelope__flap{background:var(--black);color:var(--paper);display:flex;justify-content:center;align-items:center}

/* notebook */
.notebook-open{display:flex;background:#2a2a2a;padding:6px}
.notebook-open__page{flex:1;background:var(--paper-soft)}
.notebook-open__page + .notebook-open__page{border-left:1px solid #cfcfcf}
.notebook-closed{background:var(--black);color:var(--paper);border-radius:4px 10px 10px 4px}
.notebook-closed__band{position:absolute;top:0;bottom:0;right:46px;width:10px;background:#e8e8e8}
</style>
</head>
<body>

<!-- Business cards -->
<section class="section section--cards">
  <div class="item card-back shadow" style="left:70px;top:250px;width:500px;height:290px" role="img" aria-label="Card back with a tonal repeat of the brand mark on black"></div>

  <article class="item card shadow" style="left:630px;top:250px;width:500px;height:290px">
    <div class="card__top">
      <div class="brand" style="font-size:14px">
        <span class="brand__square"></span>
        <span class="brand__name">Brightnest<br>Dwelling</span>
      </div>
    </div>
    <div class="card__rule"></div>
    <div class="card__bottom">
      <div>
        <p class="card__person-name">Nolan Vareck</p>
        <p class="card__person-role">Managing Director</p>
        <ul class="contact">
          <li><svg viewBox="0 0 10 10"><path d="M2 1l2 2-1 1.2a6 6 0 0 0 2.8 2.8L7 6l2 2-1.2 1.2C4.5 9 1 5.5.8 2.2z" fill="currentColor"/></svg>+1 555 014 2290</li>
          <li><svg viewBox="0 0 10 10"><rect x=".5" y="2" width="9" height="6" fill="currentColor"/><path d="M.5 2l4.5 3.4L9.5 2" stroke="#fff" fill="none" stroke-width=".8"/></svg>hello@brightnestdwelling.com</li>
          <li><svg viewBox="0 0 10 10"><circle cx="5" cy="5" r="4.2" fill="none" stroke="currentColor"/><path d="M.8 5h8.4M5 .8c-2 2.5-2 5.9 0 8.4M5 .8c2 2.5 2 5.9 0 8.4" stroke="currentColor" fill="none" stroke-width=".7"/></svg>www.brightnestdwelling.com</li>
        </ul>
      </div>
      <p class="card__address">Brightnest Dwelling Ltd.<br>48 Alder Crest Lane,<br>Oakmere, ON K2P 7R4</p>
    </div>
  </article>
</section>

<!-- Stationery suite -->
<section class="section section--suite">
  <article class="item letter shadow" style="left:298px;top:70px;width:295px;height:425px;padding:24px 24px 20px">
    <div class="brand" style="font-size:6.5px;align-items:flex-start;margin-bottom:18px">
      <span class="brand__square"></span>
      <span class="brand__name" style="text-align:left">Brightnest<br>Dwelling</span>
    </div>
    <div class="letter__body">
      <p>Dear customer,</p>
      <p>Thank you for choosing us for your stay. Our team prepares every room with care so that each visit feels calm, comfortable and personal from the moment you arrive.</p>
      <p>Flexible terms let you book a single night or a full season. Every apartment includes fast internet, fresh linen, weekly cleaning and a quiet workspace for business guests.</p>
      <p>Our front desk is open every day and can arrange transport, meeting rooms and late check out on request. Please contact us with any question before your arrival.</p>
      <p>We look forward to welcoming you soon.</p>
      <p>Yours Sincerely,</p>
      <div class="signature" role="img" aria-label="Handwritten signature"></div>
    </div>
    <div class="letter__foot">
      <span>+1 555 014 2290<br>hello@brightnestdwelling.com<br>www.brightnestdwelling.com</span>
      <span style="text-align:right">Brightnest Dwelling Ltd.<br>48 Alder Crest Lane,<br>Oakmere, ON K2P 7R4</span>
    </div>
  </article>

  <article class="item folder shadow" style="left:645px;top:50px;width:348px;height:440px;padding-top:130px">
    <div class="brand" style="font-size:22px">
      <span class="brand__square" style="width:3.6em;height:3.6em"></span>
      <span class="brand__name">Brightnest<br>Dwelling</span>
    </div>
    <div class="folder__band">www.brightnestdwelling.com</div>
  </article>

  <div class="item card-back shadow" style="left:190px;top:526px;width:132px;height:76px" role="img" aria-label="Card back with a tonal repeat of the brand mark on black"></div>
  <article class="item card shadow" style="left:190px;top:622px;width:132px;height:76px;padding:7px 8px">
    <div class="card__top"><div class="brand" style="font-size:4.5px"><span class="brand__square"></span><span class="brand__name">Brightnest<br>Dwelling</span></div></div>
    <div class="card__bottom" style="font-size:3.6px;line-height:1.4">
      <span><b>NOLAN VARECK</b><br>Managing Director<br>+1 555 014 2290<br>www.brightnestdwelling.com</span>
      <span style="text-align:right">48 Alder Crest Lane,<br>Oakmere, ON K2P 7R4</span>
    </div>
  </article>

  <article class="item envelope shadow" style="left:358px;top:538px;width:345px;height:158px;padding:22px 0 0 30px">
    <div class="brand" style="font-size:6.5px;align-items:flex-start">
      <span class="brand__square"></span>
      <span class="brand__name" style="text-align:left">Brightnest<br>Dwelling</span>
      <span style="font-size:5px;line-height:1.4;color:var(--grey-text)">48 Alder Crest Lane,<br>Oakmere,<br>ON K2P 7R4</span>
    </div>
  </article>

  <article class="item envelope shadow" style="left:722px;top:538px;width:330px;height:158px">
    <div class="envelope__flap" style="height:50px;font-size:6px">
      <div class="brand"><span class="brand__square" style="width:2.6em;height:2.6em"></span></div>
    </div>
  </article>
</section>

<!-- A4 letterhead and envelope -->
<section class="section section--a4">
  <article class="item letter shadow" style="left:133px;top:161px;width:448px;height:612px;padding:48px 0 0 48px">
    <div class="brand" style="font-size:11px;align-items:flex-start">
      <span class="brand__square"></span>
      <span class="brand__name" style="text-align:left">Brightnest<br>Dwelling</span>
      <span style="font-size:8px;line-height:1.4;color:var(--grey-text)">48 Alder Crest Lane,<br>Oakmere,<br>ON K2P 7R4</span>
    </div>
  </article>

  <article class="item envelope shadow" style="left:632px;top:133px;width:448px;height:640px;background:var(--paper)">
    <div class="envelope__flap" style="height:68px;border-radius:24px 24px 0 0"></div>
    <div class="brand" style="font-size:24px;color:var(--faint);position:absolute;left:0;right:0;top:230px">
      <span class="brand__square" style="width:3em;height:3em"></span>
      <span class="brand__name">Brightnest<br>Dwelling</span>
    </div>
  </article>
</section>

<!-- Notebooks -->
<section class="section section--notebook">
  <article class="item notebook-open shadow" style="left:140px;top:210px;width:540px;height:370px">
    <div class="notebook-open__page" style="padding:26px">
      <div class="brand" style="font-size:6px;align-items:flex-start"><span class="brand__square"></span></div>
    </div>
    <div class="notebook-open__page"></div>
  </article>

  <article class="item notebook-closed shadow" style="left:730px;top:150px;width:340px;height:450px">
    <div class="notebook-closed__band"></div>
    <div class="brand" style="font-size:15px;position:absolute;left:0;right:56px;top:130px">
      <span class="brand__square" style="width:3em;height:3em"></span>
      <span class="brand__name">Brightnest<br>Dwelling</span>
    </div>
    <p style="position:absolute;left:0;right:56px;bottom:60px;text-align:center;font-size:9px;letter-spacing:.1em">www.brightnestdwelling.com</p>
  </article>
</section>

</body>
</html>
```